Web Design Project for Film Business

We need a web design for a new company based in Bondi Beach, Sydney, Australia. We basically provide filming and video editing services. Our targets are basically corporate videos, wedding videos and other types of functions.
The important thing to know about us is that we are not just people that press the record button, we consider ourselves story tellers. We can make something boring like a conference look interesting to watch and we can also make a wedding look like a blockbuster movie that you can't look away from until its finished.
We need something as new and fresh as Bondi Beach. A young place where people come from all over the world to enjoy summer and we are lucky to be based here.
To see some of our work please visit our tavlora Channel. Make sure you watch a couple of wedding video and the corporate video so you can have a better understanding about our style.
Please note- we are not trying to market ourselves exclusively as wedding videographers, nor do we want to exploit the idea of the beach.

http://tavlora.com/channels/815374

sites that we really like:

http://www.quillpathreels.co.uk/
http://www.marnowebb.co.uk/

Target Market(s)

Couples - Corporate

Industry/Entity Type

Business

Requirements
Must have
• 5 to 6 pages (we are still deciding)
-main page
-our story (story about Karrow Films)
-your story (page designated for wedding videos)
-your business (page designated for corporate videos)
-contact us
-other stuff
Nice to have
• I would like to see some animation. Maybe you can animate our logo. Up to the designer

```html
<!DOCTYPE html>
<html lang="en">
<head>
<meta charset="utf-8">
<title>Karrow Films – The Art of Filming</title>
<link href="https://fonts.googleapis.com/css2?family=Questrial&family=Cinzel:wght@400&family=Italianno&display=swap" rel="stylesheet">
<style>
  :root{
    --night:#1c1a1b;
    --night-deep:#0f0e0e;
    --panel:#1a1819;
    --plum:#8a4d66;
    --plum-dark:#7a4157;
    --plum-line:#7d4a5c;
    --ink:#1d1d1d;
    --grey:#9a9a9a;
    --grey-dim:#4e4c4d;
    --paper:#ffffff;
    --stripe:#ededed;
    --sky:#4a78b8;
  }
  *{box-sizing:border-box;margin:0;padding:0}
  html,body{width:1200px;height:950px;overflow:hidden}
  body{position:relative;background:var(--night);font-family:Arial,Helvetica,sans-serif;color:var(--ink)}
  .abs{position:absolute}
  .heading{font-family:"Questrial",sans-serif;font-weight:400}
  .accent{color:var(--plum)}

  /* bands */
  .band-top{left:0;top:0;width:1200px;height:390px;background:linear-gradient(#1e1c1d,#151314)}
  .band-top::before{content:"";position:absolute;left:0;right:0;top:4px;height:6px;border-top:1px solid #2c2a2b;border-bottom:1px solid #2c2a2b}
  .band-mid{left:0;top:390px;width:1200px;height:360px;background:repeating-linear-gradient(90deg,var(--stripe) 0 20px,#fff 20px 40px)}
  .band-foot{left:0;top:750px;width:1200px;height:200px;background:repeating-linear-gradient(45deg,#1f1d1e 0 2px,#1a1819 2px 4px)}

  /* utility bar */
  .utility{left:853px;top:0;width:205px;height:29px;background:#2a2a2e;font-family:"Questrial",sans-serif;font-size:12px;color:#fff;display:flex;align-items:center;justify-content:center;gap:8px}
  .utility a{color:#fff;text-decoration:none}
  .utility .login{color:#c9c9c9}

  /* brand */
  .brand{left:143px;top:0;width:176px;height:158px}
  .brand-name{left:143px;top:42px;width:176px;text-align:center;font-family:"Questrial",sans-serif;font-size:30px;line-height:32px;color:#1d1d1d;letter-spacing:1px}

  /* nav */
  .nav-rule{left:340px;top:90px;width:860px;height:1px;background:#3a3839}
  .nav{top:66px;font-family:"Questrial",sans-serif;font-size:16px;color:var(--grey);text-decoration:none}
  .nav.current{color:var(--plum);border-bottom:3px solid #6b6869;padding-bottom:1px}

  /* hero */
  .hero-frame{left:125px;top:70px;width:215px;height:30px;background:#111}
  .hero-visual{left:125px;top:100px;width:728px;height:290px;background:radial-gradient(ellipse at 60% 35%,#8a7562 0%,#5a4a3e 35%,#2e2620 70%,#1a1512 100%)}
  .hero-the{left:223px;top:178px;font-family:"Cinzel",serif;font-size:13px;color:#c99aa6;writing-mode:vertical-rl;transform:rotate(180deg);letter-spacing:2px}
  .hero-art{left:238px;top:166px;font-family:"Cinzel",serif;font-size:54px;line-height:58px;color:#fff}
  .hero-of{left:345px;top:188px;font-family:"Italianno",cursive;font-size:30px;color:#b8788f}
  .hero-filming{left:238px;top:214px;font-family:"Cinzel",serif;font-size:54px;line-height:58px;color:#fff}
  .hero-bar{left:125px;top:390px;width:285px;height:7px;background:var(--plum-line)}
  .hero-rule{left:410px;top:390px;width:665px;height:2px;background:var(--plum-line)}

  /* side panel */
  .side{left:853px;top:95px;width:222px;height:295px;background:var(--panel)}
  .side-title{left:867px;top:96px;font-size:19px;color:#4f4d4e}
  .side-mark{left:850px;top:134px;width:8px;height:46px;background:var(--plum-dark)}
  .side-photo{left:868px;top:134px;width:207px;height:46px;background:linear-gradient(#4f86cc 0%,#8fb3df 55%,#2a3b52 75%,#101820 100%)}
  .side-text{left:868px;top:187px;width:200px;font-size:11px;line-height:13px;color:#5f5d5e}
  .side-link{font-size:11px;color:var(--plum);text-decoration:none;letter-spacing:.3px}
  .about{left:837px;top:251px;width:238px;height:69px;background:var(--night-deep)}
  .about::before{content:"";position:absolute;left:0;top:18px;width:28px;height:1px;background:#666}
  .about-title{left:868px;top:257px;font-size:18px;color:#fff}
  .about-text{left:869px;top:283px;width:200px;font-size:11px;line-height:13px;color:#8a8889}

  /* content */
  .sheet{left:125px;top:390px;width:950px;height:396px;background:var(--paper);box-shadow:0 0 18px rgba(0,0,0,.15)}
  .page-title{left:151px;top:411px;font-size:18px}
  .text-size{left:1024px;top:416px;display:flex;align-items:baseline;gap:8px;color:#111;font-family:Arial,sans-serif}
  .lead{left:150px;top:449px;width:900px;font-size:11.5px;line-height:14px;color:#111}
  .section-title{font-size:18px}
  .story-box{left:151px;top:565px;width:259px;height:68px;background:#231f20}
  .story-thumb{left:159px;top:573px;width:90px;height:126px;background:linear-gradient(135deg,#3a3520,#9a8a40 40%,#3b3a35 70%,#1a1a1a)}
  .story-head{left:263px;top:570px;font-size:18px;line-height:22px;color:#fff}
  .story-underline{left:263px;top:617px;width:37px;height:2px;background:var(--plum)}
  .story-text{left:263px;top:635px;width:140px;font-size:12px;line-height:13.3px;font-weight:bold;color:#222}
  .mini-links{top:717px;font-size:10.5px;line-height:12px;color:#333;list-style:none}
  .mini-divider{left:270px;top:719px;width:1px;height:36px;background:var(--plum)}
  .up{left:248px;top:762px;width:44px;height:44px;transform:rotate(45deg);background:linear-gradient(135deg,#a46a83,#6f3b52);border:2px solid #c99aae}
  .up-label{left:257px;top:792px;width:26px;text-align:center;font-size:10px;color:#fff}
  .up-arrow{left:263px;top:766px}
  .news-rule{left:446px;top:566px;width:629px;height:1px;background:#ddd}
  .news-thumb{width:55px;height:55px;background:linear-gradient(#d8d8d8,#8a8a8a 45%,#3a3a3a 60%,#e8e8e8)}
  .news-title{font-size:11.5px;font-weight:bold;color:var(--plum)}
  .news-body{width:180px;font-size:11.5px;line-height:13.3px;color:#111}
  .more{font-size:11.5px;color:var(--plum);letter-spacing:.5px;text-decoration:none}
  .tagline{left:410px;top:734px;font-family:"Italianno",cursive;font-size:44px;color:var(--plum-dark);white-space:nowrap}

  /* footer */
  .foot-rule{height:2px;background:var(--plum-line)}
  .foot-thin{height:1px;background:var(--plum-line)}
  .foot-title{top:806px;font-size:19px;color:#7a7879}
  .foot-text{left:410px;top:832px;width:160px;font-size:11.5px;line-height:13px;color:#4b494a}
  .news-note{left:610px;top:833px;width:165px;font-size:9.5px;line-height:12px;color:#8a8889}
  .email{left:609px;top:860px;width:161px;height:23px;background:#151314;border:1px solid #5a3545;color:#aaa;font-size:10.5px;text-align:center;line-height:21px}
  .submit{left:705px;top:886px;width:64px;height:20px;background:var(--plum-dark);color:#fff;font-size:11px;text-align:center;line-height:20px}
  .social{left:809px;top:836px;display:flex;gap:9px}
  .social-item{width:30px;text-align:center;font-size:7.5px;color:#9a9899}
  .social-item span{display:block;width:30px;height:22px;background:#5a5758;border-radius:3px;margin-bottom:2px}
  .copyright{left:172px;top:923px;font-size:8px;color:var(--plum-line)}
</style>
</head>
<body>
  <div class="abs band-top"></div>
  <div class="abs band-mid"></div>
  <div class="abs band-foot"></div>

  <nav class="abs utility"><a class="login" href="#">Login</a>|<a href="#">Register</a>|<a href="#">Sitemap</a></nav>

  <!-- header -->
  <div class="abs hero-frame"></div>
  <div class="abs hero-visual" role="img" aria-label="Close-up photograph of a film clapperboard in warm sepia light"></div>
  <svg class="abs brand" viewBox="0 0 176 158" aria-hidden="true"><polygon points="0,0 176,0 176,90 88,158 0,90" fill="#fff"/></svg>
  <div class="abs brand-name">KARROW<br>FILMS</div>

  <div class="abs nav-rule"></div>
  <a class="abs nav current" href="#" style="left:354px">Homepage</a>
  <a class="abs nav" href="#" style="left:465px">Our story</a>
  <a class="abs nav" href="#" style="left:551px">Your story</a>
  <a class="abs nav" href="#" style="left:650px">Your business</a>
  <a class="abs nav" href="#" style="left:773px">Contact us</a>

  <div class="abs hero-the">THE</div>
  <div class="abs hero-art">ART</div>
  <div class="abs hero-of">of</div>
  <div class="abs hero-filming">FILMING</div>

  <aside class="abs side"></aside>
  <h2 class="abs heading side-title">Our Philosophy</h2>
  <div class="abs side-mark"></div>
  <div class="abs side-photo" role="img" aria-label="Photograph of a blue evening sky over a coastline"></div>
  <p class="abs side-text">Lorem ipsum dolor sit amet,<br>consectetur adipisicing elit, sed do<br>eiusmod tempor incididunt ut<br><a class="side-link" href="#" style="line-height:24px">Read More &gt;&gt;</a></p>
  <div class="abs about"></div>
  <h2 class="abs heading about-title">About us</h2>
  <p class="abs about-text">Lorem ipsum dolor sit amet,<br>consectetur adipisicing elit, sed do<br>eiusmod tempor incididunt ut<br>labore et dolore magna aliqua. Ut<br>enim ad minim veniam,<br>quis nostrud exercitation ullamco</p>
  <a class="abs side-link" href="#" style="left:870px;top:371px">Find out more&gt;&gt;</a>

  <!-- content -->
  <main class="abs sheet"></main>
  <div class="abs hero-bar"></div>
  <div class="abs hero-rule"></div>

  <h1 class="abs heading page-title"><span class="accent">Page</span> Title</h1>
  <div class="abs text-size"><span style="font-size:10px">A</span><span style="font-size:13px">A</span><span style="font-size:17px">A</span></div>
  <p class="abs lead">Lorem ipsum dolor sit amet, consectetur adipisicing elit, sed do eiusmod tempor incididunt ut labore et dolore magna aliqua. Ut enim ad minim veniam, quis nostrud exercitation ullamco laboris nisi ut aliquip ex ea commodo consequat. Duis aute irure dolor in reprehenderit in voluptate velit esse cillum dolore eu fugiat nulla pariatur. Excepteur sint occaecat cupidatat non proident, sunt in culpa qui officia deserunt mollit anim id est laborum</p>

  <h2 class="abs heading section-title" style="left:151px;top:531px"><span class="accent">Our</span> Story</h2>
  <div class="abs story-box"></div>
  <div class="abs story-thumb" role="img" aria-label="Photograph of a film reel and strip in golden light"></div>
  <h3 class="abs heading story-head">The story of<br>Karrow Films</h3>
  <div class="abs story-underline"></div>
  <p class="abs story-text">Lorem ipsum dolor sit amet, consectetur adipi-sicing elit, sed do eius-mod tempor incididunt ut labore et dolore</p>

  <ul class="abs mini-links" style="left:158px"><li>Tell a friend</li><li>Social Media</li><li>Sitemap</li></ul>
  <div class="abs mini-divider"></div>
  <ul class="abs mini-links" style="left:288px"><li>Login</li><li>Register</li><li>Logout</li><li>My Page</li></ul>

  <h2 class="abs heading section-title" style="left:446px;top:531px"><span class="accent">Latest</span> News</h2>
  <div class="abs news-rule"></div>

  <div class="abs news-thumb" style="left:447px;top:578px" role="img" aria-label="Photograph of a curled strip of film"></div>
  <h3 class="abs news-title" style="left:514px;top:575px">Lorem ipsum dolor sit amet</h3>
  <p class="abs news-body" style="left:514px;top:599px">Lorem ipsum dolor sit amet, consectetur adipisicing elit, sed do eiusmod tempor incidi-dunt ut labore et dolore magna aliqua. Ut enim ad minim veniam, quis nostrud exercitation ullamco laboris nisi ut aliquip</p>
  <a class="abs more" href="#" style="left:514px;top:714px">MORE &gt;&gt;</a>

  <div class="abs news-thumb" style="left:737px;top:578px" role="img" aria-label="Photograph of a curled strip of film"></div>
  <h3 class="abs news-title" style="left:804px;top:575px">Lorem ipsum dolor sit amet</h3>
  <p class="abs news-body" style="left:804px;top:599px">Lorem ipsum dolor sit amet, consectetur adipisicing elit, sed do eiusmod tempor incidi-dunt ut labore et dolore magna aliqua. Ut enim ad minim veniam, quis nostrud exercitation ullamco laboris nisi ut aliquip</p>
  <a class="abs more" href="#" style="left:804px;top:714px">MORE &gt;&gt;</a>

  <p class="abs tagline">We consider ourselves story tellers. Let us tell your story...</p>

  <div class="abs up"></div>
  <svg class="abs up-arrow" width="14" height="24" viewBox="0 0 14 24" aria-hidden="true"><path d="M7 2 L7 22" stroke="#fff" stroke-width="1" stroke-dasharray="2 2"/><path d="M3 6 L7 2 L11 6" fill="none" stroke="#fff" stroke-width="1.4"/></svg>
  <div class="abs up-label">up</div>

  <!-- footer -->
  <div class="abs foot-rule" style="left:410px;top:785px;width:665px"></div>
  <div class="abs foot-rule" style="left:88px;top:785px;width:37px"></div>

  <h2 class="abs heading foot-title" style="left:410px"><span class="accent">Other</span>Stuff</h2>
  <p class="abs foot-text">Lorem ipsum dolor sit amet, consectetur adipisicing elit, sed do eiusmod tempor incididunt ut labore et dolore magna aliqua. Ut enim ad minim veniam, quis nostrud exercitation</p>

  <h2 class="abs heading foot-title" style="left:609px"><span class="accent">News</span>Letter</h2>
  <p class="abs news-note">be the first to know about our latest projects and news</p>
  <div class="abs email">Enter your e-mail here</div>
  <div class="abs submit">Submit</div>

  <h2 class="abs heading foot-title" style="left:809px"><span class="accent">Like</span> Watch <span class="accent">Follow</span></h2>
  <div class="abs social">
    <div class="social-item"><span></span>Folkline</div>
    <div class="social-item"><span></span>Murmur</div>
    <div class="social-item"><span></span>Reelhub</div>
    <div class="social-item"><span></span>Snapfold</div>
    <div class="social-item"><span></span>tavlora</div>
    <div class="social-item"><span></span>Markly</div>
  </div>

  <div class="abs foot-thin" style="left:410px;top:928px;width:665px"></div>
  <div class="abs foot-thin" style="left:88px;top:928px;width:37px"></div>
  <p class="abs copyright">Copyright 2011-12 <span style="color:#b0788f">KARROW FILMS</span> - All rights reserved</p>
</body>
</html>
```